1 Page Website Responsive HTML Refresh

My website was designed on the fly and is not representative of our brand in the market. (www.tallowreed.com.au)

I have a coder who can turn your design into real life - I just need the PSD files created for him to work to. It should align to our corporate flyer - I have attached the files.

The site should just be a single page and has 4 sections:

1. Hero Image and Intro
2. For Businesses
3. For Residents
4. Contact

The content can be taken from the live website, however there are a few changes to be made, that will impact your design:

For Businesses: Remove the call to action email box and all the content that is about "Just for Small Business"

For Residents: Remove #3 Product Diversity, so there are just 4 reasons.

Please add in a section that shows the areas that Tallow Reed is currently active in. These are:

Indooroopilly & Surrounds
Ascot & Surrounds
North Lakes & Surrounds
South Brisbane & Surrounds
Springfield & Surrounds
Browns Plains & Surrounds
Redcliffe & Surrounds

I am looking for something clean and modern that is aligned to our flyer.

Target Market(s)

Small business owners reviewing the site to establish credibility with our business.

Industry/Entity Type

Advertising

Number of Pages Required

1 page

Font styles to use
Sans Serif

Colors
abd036

Requirements
Must have
• The site must include an image of the publication so people see what it looks like and a sample of the FB page image too (images are in attachment)
• Must use my corporate colour of green as the major highlight colour.
Nice to have
• Open to clean, modern and professional design. Good use of white space. Not cluttered or too busy

```html
<!DOCTYPE html>
<html lang="en">
<head>
<meta charset="utf-8">
<title>Tallow Reed – Connecting local businesses with local residents</title>
<link href="https://fonts.googleapis.com/css2?family=Open+Sans:wght@400;600;700&family=Raleway:wght@400;600;700&display=swap" rel="stylesheet">
<style>
:root{
  --green:#a2d01f;
  --green-dark:#8fbc12;
  --ink:#222222;
  --text:#444444;
  --grey-band:#efefef;
  --area-box:#eeeeee;
  --footer:#1f1f1f;
  --white:#ffffff;
}
*{box-sizing:border-box;margin:0;padding:0}
html,body{width:1200px;height:3949px;overflow:hidden}
body{font-family:"Open Sans",Arial,sans-serif;color:var(--text);background:var(--white);font-size:13px;line-height:1.55}
h1,h2,h3,h4{font-family:"Raleway","Open Sans",sans-serif}
.wrap{width:880px;margin:0 auto;position:relative}

/* header */
.site-header{height:115px;border-top:5px solid var(--green);background:var(--white)}
.site-header .wrap{height:110px;display:flex;align-items:center;justify-content:space-between}
.brand{display:flex;align-items:center;gap:10px}
.brand-dot{width:34px;height:34px;border-radius:50%;background:var(--green)}
.brand-name{font-family:"Raleway",sans-serif;font-weight:700;font-size:28px;color:var(--ink)}
.call{font-size:17px;color:var(--ink)}
.main-nav{height:37px;background:var(--green)}
.main-nav .wrap{height:37px;display:flex;align-items:center;justify-content:space-between}
.nav-links{display:flex;list-style:none;height:37px}
.nav-links li{font-size:12px;font-weight:700;color:var(--white);padding:0 14px;line-height:37px}
.nav-links li.active{background:var(--green-dark)}
.social{display:flex;gap:6px}
.social span{width:22px;height:22px;background:var(--ink);display:block}

/* hero */
.hero{height:448px;background:linear-gradient(180deg,#6b9cc9 0%,#a8c9e4 38%,#8c9aa6 62%,#3c5a6c 78%,#2a5a7c 100%);text-align:center;color:var(--white);padding-top:170px}
.hero h1{font-size:32px;font-weight:600}
.hero .tagline{font-size:19px;letter-spacing:.5px;margin-top:2px}
.hero-buttons{display:flex;justify-content:center;gap:14px;margin-top:28px}
.btn{background:var(--green);color:var(--white);font-size:13px;font-weight:600;padding:7px 18px;display:inline-block}

/* bands */
.band-green{background:var(--green);color:var(--white);text-align:center}
.band-grey{background:var(--grey-band);text-align:center}
.band-white{background:var(--white);text-align:center}
.section-title{color:var(--green);font-size:19px;font-weight:700}

.intro{height:248px;padding-top:78px}
.intro p{font-size:11px;line-height:1.6;width:860px;margin:0 auto}
.intro .strong-line{color:var(--ink);font-family:"Raleway",sans-serif;font-weight:700;font-size:16px;margin-top:28px}

.businesses{height:211px;padding-top:74px}
.businesses p{font-size:11px;line-height:1.6;margin-top:8px}

.questions{height:368px;padding-top:82px}
.team{display:flex;justify-content:center;gap:18px}
.team .avatar{width:75px;height:75px;border-radius:50%;border:3px solid var(--green);background:linear-gradient(160deg,#d9b59b,#8a6a55)}
.question-list{list-style:none;margin-top:18px}
.question-list li{color:var(--green);font-size:17px;line-height:23px}

.reasons{height:413px;padding-top:58px}
.reasons .section-title{font-size:18px;text-transform:uppercase}
.reason-grid{display:grid;grid-template-columns:repeat(3,300px);justify-content:space-between;row-gap:24px;margin-top:18px}
.reason svg{width:40px;height:34px;display:block;margin:0 auto}
.reason h4{color:var(--green);font-size:13px;font-weight:700;text-transform:uppercase;margin-top:2px}
.reason p{font-size:11.5px;line-height:1.5}

.residents{height:253px;padding-top:82px}
.residents h2{color:var(--ink);font-size:19px;font-weight:700}
.residents p{font-size:11px;line-height:1.6;margin-top:6px}

.community{height:427px;padding-top:76px}
.community .section-title{font-size:17px;text-transform:uppercase;line-height:1.5}
.community-grid{display:grid;grid-template-columns:repeat(4,210px);justify-content:space-between;margin-top:42px}
.num{width:44px;height:44px;border-radius:50%;background:var(--green);border:3px solid var(--ink);color:var(--ink);font-weight:700;font-size:17px;line-height:38px;margin:0 auto}
.community-item h4{color:var(--ink);font-size:14px;font-weight:700;margin-top:6px}
.community-item p{font-size:11.5px;line-height:1.5}

.areas{height:360px;padding-top:107px}
.area-grid{display:grid;grid-template-columns:repeat(3,280px);justify-content:space-between;row-gap:9px}
.area{background:var(--area-box);color:var(--green);font-size:17px;height:48px;line-height:48px}
.area.center{grid-column:2}

/* contact */
.contact{height:760px;padding-top:76px;color:var(--ink)}
.contact h2{font-size:19px;font-weight:700}
.map{width:880px;height:259px;margin:18px auto 0;background:linear-gradient(135deg,#e6e2d6,#d7d3c6 50%,#e9dcae);position:relative}
.map-pin{position:absolute;left:220px;top:38px}
.contact-row{display:flex;justify-content:space-between;margin-top:29px;text-align:left}
.contact-form{width:280px}
.field{background:var(--white);height:32px;margin-bottom:13px;font-size:11px;color:#777;padding:7px 10px}
.field.message{height:88px}
.submit{display:block;width:110px;margin:10px 0 0 165px;background:var(--ink);color:var(--white);font-size:12px;font-weight:700;text-align:center;line-height:30px}
.city-photo{width:294px;height:232px;background:linear-gradient(180deg,#4f8fd0,#a9cde9 45%,#56606a 70%,#2f5d84);border:6px solid var(--white)}
.info-card{width:227px;height:222px;background:var(--white);padding:26px 16px;font-size:11.5px;line-height:1.75}
.info-card b{color:var(--green);font-weight:600}

/* footer */
.site-footer{height:253px;background:var(--footer);color:#dddddd;font-size:11.5px;padding-top:53px}
.footer-cols{display:flex}
.footer-about{width:301px}
.footer-about p+p{margin-top:14px}
.footer-links{width:126px;list-style:none}
.footer-info{width:300px}
.footer-info h4{color:var(--green);font-family:"Open Sans",sans-serif;font-size:13px;font-weight:700}
.footer-info b{color:var(--green);font-weight:400}
.footer-social{display:flex;gap:9px;margin-left:auto}
.footer-social span{width:27px;height:27px;background:var(--green);display:block}
.copyright{height:56px;line-height:56px;text-align:center;font-size:11px;color:var(--ink)}
.copyright b{color:var(--green);font-weight:400}
</style>
</head>
<body>

<header class="site-header">
  <div class="wrap">
    <div class="brand"><span class="brand-dot"></span><span class="brand-name">Tallow Reed</span></div>
    <div class="call">Call Now 1300 555 019</div>
  </div>
</header>
<nav class="main-nav">
  <div class="wrap">
    <ul class="nav-links">
      <li class="active">Home</li><li>For Businesses</li><li>For Residents</li><li>Contact</li>
    </ul>
    <div class="social"><span></span><span></span><span></span><span></span></div>
  </div>
</nav>

<section class="hero" role="img" aria-label="City skyline across the river under a blue sky">
  <h1>It's time to Tallow Reed</h1>
  <div class="tagline">CONNECTING LOCAL BUSINESSES WITH LOCAL RESIDENTS</div>
  <div class="hero-buttons"><span class="btn">For Business</span><span class="btn">For Residents</span></div>
</section>

<section class="band-green intro">
  <p>A vibrant community is such a huge part of the local fabric of our world.<br>
  By engaging with the people who work and live around you, you can actively contribute to making your local area a better place. Tallow Reed is a platform that helps connect local businesses with local residents. It offers a cost effective way for business owners to communicate with their ideal customers, and provides information, news and special offers that are relevant to the people who live in the area.</p>
  <p class="strong-line">Tallow Reed &amp; connect with your community.</p>
</section>

<section class="band-white businesses">
  <div class="wrap">
    <h2 class="section-title">For Businesses</h2>
    <p>Tallow Reed is a marketing and advertising solution designed just for small business. Combining expert guidance around marketing strategy, with locally focused digital and print advertising, Tallow Reed provides a holistic and cost effective solution that is revolutionising the way small businesses connect with their potential customers.</p>
  </div>
</section>

<section class="band-grey questions">
  <div class="team">
    <span class="avatar" role="img" aria-label="Team member portrait"></span>
    <span class="avatar" role="img" aria-label="Team member portrait"></span>
    <span class="avatar" role="img" aria-label="Team member portrait"></span>
  </div>
  <ul class="question-list">
    <li>Wish there was a more cost-effective way to advertise your business?</li>
    <li>Struggle to find the time to tackle marketing?</li>
    <li>Needing some advice from a marketing professional?</li>
    <li>Know you need to be doing more marketing?</li>
    <li>Want a way to connect with customers in your local area?</li>
  </ul>
</section>

<section class="band-white reasons">
  <div class="wrap">
    <h2 class="section-title">6 Reasons your business needs Tallow Reed</h2>
    <div class="reason-grid">
      <div class="reason">
        <svg viewBox="0 0 40 34"><path d="M6 13h8l16-9v26L14 21H6z" fill="#222"/><rect x="9" y="21" width="5" height="9" fill="#222"/><path d="M33 12l5-3M33 17h6M33 22l5 3" stroke="#222" stroke-width="2"/></svg>
        <h4>Marketing + Advertising</h4>
        <p>Combines both marketing strategy and advertising execution to provide a more cohesive and effective way to promote your business.</p>
      </div>
      <div class="reason">
        <svg viewBox="0 0 40 34"><rect x="5" y="6" width="30" height="20" rx="2" fill="#222"/><circle cx="20" cy="16" r="5" fill="#fff"/><circle cx="31" cy="26" r="6" fill="#fff" stroke="#222" stroke-width="2"/><path d="M28 26l2 2 4-4" stroke="#222" stroke-width="2" fill="none"/></svg>
        <h4>Small Business Value</h4>
        <p>Fully inclusive of consulting, design and production and it costs less than 15c per household.</p>
      </div>
      <div class="reason">
        <svg viewBox="0 0 40 34"><path d="M5 4h30l3 9H2z" fill="#222"/><rect x="6" y="15" width="28" height="16" fill="#222"/><rect x="10" y="19" width="8" height="12" fill="#fff"/><rect x="22" y="19" width="8" height="7" fill="#fff"/></svg>
        <h4>Showcasing Your Business</h4>
        <p>Focuses on your story as well as your products and services to help you really connect with your local customer base.</p>
      </div>
      <div class="reason">
        <svg viewBox="0 0 40 34"><rect x="4" y="7" width="32" height="22" fill="#222"/><path d="M4 7l16 13 16-13" stroke="#fff" stroke-width="2" fill="none"/></svg>
        <h4>Direct Mail + Social Media</h4>
        <p>Leverages the most cost effective and proven online and offline methods to get your brand out in the market.</p>
      </div>
      <div class="reason">
        <svg viewBox="0 0 40 34"><circle cx="20" cy="9" r="5" fill="#222"/><circle cx="9" cy="13" r="4" fill="#222"/><circle cx="31" cy="13" r="4" fill="#222"/><path d="M11 28a9 9 0 0118 0z" fill="#222"/><path d="M2 28a7 7 0 0112-4v4zM38 28a7 7 0 00-12-4v4z" fill="#222"/></svg>
        <h4>Your Ideal Customer</h4>
        <p>Targets only people in your local area so you can create long term relationships and repeat business.</p>
      </div>
      <div class="reason">
        <svg viewBox="0 0 40 34"><circle cx="19" cy="18" r="13" fill="none" stroke="#222" stroke-width="3"/><circle cx="19" cy="18" r="7" fill="none" stroke="#222" stroke-width="3"/><circle cx="19" cy="18" r="2" fill="#222"/><path d="M19 18L35 3" stroke="#222" stroke-width="2"/></svg>
        <h4>Rely on the Experts</h4>
        <p>Makes your advertising and marketing activities effective, easy and stress free, allowing you to focus on running your business.</p>
      </div>
    </div>
  </div>
</section>

<section class="band-green residents">
  <div class="wrap">
    <h2>For Residents</h2>
    <p>Keep a look out in your letterbox each quarter for Tallow Reed. It's jam packed with offers and details on businesses that are just around the corner from you. With Tallow Reed you can get to know the staff and owners, find out about new products and services and learn what businesses are doing to support your local area. For detailed information on what is happening in your neighbourhood delivered digitally, be sure to follow the Tallow Reed social page for your area. This page is like a community hub where you can find details on events, news that is locally focused, extra specials and deals local businesses want to share, and the chance to win prizes.</p>
  </div>
</section>

<section class="band-grey community">
  <div class="wrap">
    <h2 class="section-title">Your support of local businesses has a very real and tangible impact on your neighborhood.<br>Here are a couple of reasons why it is great to Tallow Reed.</h2>
    <div class="community-grid">
      <div class="community-item">
        <div class="num">1</div>
        <h4>Unique Communities</h4>
        <p>You chose to live in your area because it offered something unique that resonated with you. It had lots of great parks, was in the catchment of a great school, or maybe it had good coffee a stone's throw away. It is that unique feel of a local area that is in part shaped by the businesses that trade there.</p>
      </div>
      <div class="community-item">
        <div class="num">2</div>
        <h4>Keeping Dollars Local</h4>
        <p>Locally owned businesses understand how important it is to support other businesses like them. They are more likely to spend a larger share of their revenue in their own backyards, further enriching the whole community and keeping the cycle of Tallow Reed going.</p>
      </div>
      <div class="community-item">
        <div class="num">3</div>
        <h4>Local Jobs</h4>
        <p>It makes sense that a locally owned businesses creates more jobs locally. This means there are more opportunities to work closer to home and your kids have more choices for their first jobs.</p>
      </div>
      <div class="community-item">
        <div class="num">4</div>
        <h4>Giving Back</h4>
        <p>You only need to see the certificates proudly placed on the walls of local businesses to know they are the ones sponsoring the local soccer club and donating prizes to the school fund-raiser. Your support of them helps them support causes in your neighbourhood.</p>
      </div>
    </div>
  </div>
</section>

<section class="band-white areas">
  <div class="wrap area-grid">
    <div class="area">Indooroopilly &amp; Surrounds</div>
    <div class="area">Ascot &amp; Surrounds</div>
    <div class="area">North Lakes &amp; Surrounds</div>
    <div class="area">South Brisbane &amp; Surrounds</div>
    <div class="area">Springfield &amp; Surrounds</div>
    <div class="area">Browns Plains &amp; Surrounds</div>
    <div class="area center">Redcliffe &amp; Surrounds</div>
  </div>
</section>

<section class="band-green contact">
  <div class="wrap">
    <h2>Contact Us</h2>
    <div class="map" role="img" aria-label="Street map showing the office location">
      <svg class="map-pin" width="26" height="36" viewBox="0 0 26 36"><path d="M13 0a13 13 0 00-13 13c0 10 13 23 13 23s13-13 13-23A13 13 0 0013 0z" fill="#222"/><circle cx="13" cy="13" r="5" fill="#fff"/></svg>
    </div>
    <div class="contact-row">
      <div class="contact-form">
        <div class="field">Name</div>
        <div class="field">Telephone</div>
        <div class="field">Email</div>
        <div class="field message">Message</div>
        <span class="submit">SUBMIT NOW</span>
      </div>
      <div class="city-photo" role="img" aria-label="City bridge and skyline by the river"></div>
      <div class="info-card">
        <b>Company:</b> tallowreed<br>
        <b>Address:</b> PO Box 512, Ferny Grove QLD 4055<br>
        <b>Telephone:</b> 1300 555 019<br>
        <b>Email:</b> info@tallowreed.com.au<br>
        <b>Website:</b> www.tallowreed.com.au<br>
        <b>ABN:</b> 47 208 115 630
      </div>
    </div>
  </div>
</section>

<footer class="site-footer">
  <div class="wrap footer-cols">
    <div class="footer-about">
      <p>Lorem ipsum dolor sit amet, consectetur adipiscing elit. Integer gravida nisl sed sapien placerat imperdiet. Aenean id est vel orci tempor dignissim. Ut ac est velit. Aliquam lorem nulla.</p>
      <p>Aliquam placerat ultrices libero, vel hendrerit orci bibendum vitae. Donec sit amet ex sollicitudin metus tincidunt convallis at vel nunc.</p>
    </div>
    <ul class="footer-links">
      <li>Home</li><li>For Business</li><li>For Residents</li><li>Contacts</li>
    </ul>
    <div class="footer-info">
      <h4>INFO CONTACT</h4>
      <b>Address:</b> PO Box 512, Ferny Grove QLD 4055<br>
      <b>Telephone:</b> 1300 555 019<br>
      <b>Email:</b> info@tallowreed.com.au
    </div>
    <div class="footer-social"><span></span><span></span><span></span><span></span></div>
  </div>
</footer>
<div class="copyright">Copyright 2016 <b>tallowreed</b>. All Rights Reserved.</div>

</body>
</html>
```